Post it Note design

POST-IT NOTE DESIGN (CONTENT)
Size recommended: 4x6 for handwriting space.
Header (Bold):
Lighting Issue Detected on Your Property
Sub-header:
During our routine night inspection, we noted the following item(s):
Checkbox List:
⬜ Building Lights Out
⬜ Pole Lights Out
⬜ Sign Not Illuminated
⬜ Other ________________________
Action Line:
We can provide a quote or dispatch service right away.
Area for notes
Contact Block (Bold & Centered):
Brovane Fixture Inc.
Service@BrovaneFixture.com
www.BrovaneFixture.com
877-514-0862
Industry/Entity Type
Electrical lighting
Colors
Designer to choose colors to be used in the design.
Look and feel
Each slider illustrates characteristics of the customer's brand and the style your logo design should communicate.

```html
<!DOCTYPE html>
<html lang="en">
<head>
<meta charset="UTF-8">
<title>Brovane Fixture Inc. – Lighting Issue Notice</title>
<link rel="stylesheet" href="https://fonts.googleapis.com/css2?family=Poppins:ital,wght@0,400;0,500;0,600;0,700;1,700&display=swap">
<style>
  :root {
    --brand-red: #e41e26;
    --brand-navy: #2b2f7e;
    --ink: #333338;
    --hint: #b3afd0;
    --note-bg-top: #fbfbfb;
    --note-bg-bottom: #eeeeee;
    --page-bg: #d6d6d6;
    --photo-light: #e9ecef;
    --photo-mid: #aeb4ba;
    --photo-dark: #6f767d;
  }
  * { margin: 0; padding: 0; box-sizing: border-box; }
  html, body {
    width: 1020px; height: 1200px; overflow: hidden;
    background: var(--page-bg);
    font-family: "Poppins", Arial, sans-serif;
  }
  .note {
    position: absolute; left: 136px; top: 40px;
    width: 748px; height: 1120px;
    background: linear-gradient(160deg, var(--note-bg-top) 0%, #f4f4f4 50%, var(--note-bg-bottom) 100%);
    overflow: hidden;
  }
  .brand {
    position: absolute; top: 58px; left: 0; width: 100%;
    text-align: center;
    font-weight: 700; font-size: 34px; color: var(--brand-red);
    line-height: 1;
  }
  .headline {
    position: absolute; top: 150px; left: 0; width: 100%;
    text-align: center;
    font-weight: 700; font-size: 31px; color: var(--brand-red);
  }
  .intro {
    position: absolute; left: 50px; top: 210px; width: 647px; height: 56px;
    border: 1.5px solid var(--brand-navy); border-bottom: none;
    border-radius: 6px 6px 0 0;
    text-align: center;
    font-weight: 500; font-size: 23px; line-height: 31px; color: var(--brand-navy);
    padding-top: 8px;
  }
  .intro-base { position: absolute; left: 50px; top: 258px; }
  .checklist {
    position: absolute; left: 81px; top: 320px; list-style: none;
  }
  .checklist li {
    display: flex; align-items: center;
    height: 44.7px;
    font-size: 23px; font-weight: 500; color: var(--ink);
  }
  .checkbox {
    width: 16px; height: 16px; border: 1.5px solid var(--ink);
    margin-right: 14px; flex: none;
  }
  .fill-line {
    display: inline-block; width: 486px; height: 2px; margin-left: 10px; margin-top: 16px;
    border-bottom: 2px dashed var(--ink);
  }
  .action {
    position: absolute; top: 532px; left: 0; width: 100%;
    text-align: center;
    font-weight: 700; font-size: 26px; line-height: 32px; color: var(--brand-red);
  }
  .notes-area {
    position: absolute; left: 69px; top: 629px; width: 608px; height: 213px;
    border: 1.5px solid var(--brand-navy); border-radius: 11px;
    display: flex; align-items: center; justify-content: center;
    font-size: 22px; color: var(--hint);
  }
  .crew-photo {
    position: absolute; left: 0; top: 884px; width: 308px; height: 236px;
    background: radial-gradient(ellipse at 55% 40%, var(--photo-light) 0%, var(--photo-mid) 55%, var(--photo-dark) 100%);
    border-top-right-radius: 120px;
  }
  .contact {
    position: absolute; left: 272px; top: 896px; width: 476px;
    text-align: center;
  }
  .contact-label {
    display: inline-block; width: 236px; height: 47px; line-height: 47px;
    border-radius: 24px; background: var(--brand-red);
    color: #fff; font-weight: 600; font-size: 28px;
  }
  .contact-company {
    margin-top: 13px;
    font-weight: 700; font-style: italic; font-size: 23px; color: var(--brand-red);
  }
  .contact-line {
    margin-top: 2px;
    font-weight: 500; font-size: 23px; line-height: 34px; color: var(--brand-navy);
  }
  .contact-phone {
    font-weight: 700; font-size: 32px; line-height: 42px; color: var(--brand-navy);
  }
</style>
</head>
<body>
  <main class="note">
    <div class="brand">Brovane Fixture Inc.</div>

    <h1 class="headline">Lighting Issue Detected on Your Property</h1>

    <p class="intro">During our routine night inspection, we noted the<br>following item(s):</p>
    <svg class="intro-base" width="648" height="20" viewBox="0 0 648 20" aria-hidden="true">
      <path d="M1 0 V2 Q1 8 7 8 H168" fill="none" stroke="#2b2f7e" stroke-width="1.5"/>
      <circle cx="170" cy="8" r="3.5" fill="#2b2f7e"/>
      <circle cx="473" cy="8" r="3.5" fill="#2b2f7e"/>
      <path d="M475 8 H641 Q647 8 647 2 V0" fill="none" stroke="#2b2f7e" stroke-width="1.5"/>
    </svg>

    <ul class="checklist">
      <li><span class="checkbox"></span>Building Lights Out</li>
      <li><span class="checkbox"></span>Pole Lights Out</li>
      <li><span class="checkbox"></span>Sign Not Illuminated</li>
      <li><span class="checkbox"></span>Other <span class="fill-line"></span></li>
    </ul>

    <p class="action">We can provide a quote or dispatch service<br>right away.</p>

    <div class="notes-area">Area for notes</div>

    <div class="crew-photo" role="img" aria-label="Photo of a technician in a bucket lift servicing a cluster of pole-mounted flood lights"></div>

    <section class="contact">
      <div class="contact-label">Contact Info</div>
      <p class="contact-company">Brovane Fixture Inc.</p>
      <p class="contact-line">Service@BrovaneFixture.com</p>
      <p class="contact-line">www.BrovaneFixture.com</p>
      <p class="contact-phone">877-514-0862</p>
    </section>
  </main>
</body>
</html>
```